Storm postcards

We need postcards for our roofing company. A recent storm hit our area and we are looking to market to those that were hit in the area. We want something that is simple, but flashy enough to get peoples attention. We are looking for something that has a good blend of flash and professional look.

Name of the company is Tolvey Building Partners LLC

Target Market(s)

Homeowners

Font styles to use
Serif

Requirements
Must have
• Phone number 480-913-2748, The storm was mostly a wind storm, some of the postcards attached are for hail but this one should focus of STORM DAMAGE.
• My business license number has to be on the postcard somewhere preferably small and hidden ROC #284063

```html
<!DOCTYPE html>
<html lang="en">
<head>
<meta charset="utf-8">
<title>Tolvey Building Partners – Storm Damage Postcard</title>
<link rel="stylesheet" href="https://fonts.googleapis.com/css2?family=Montserrat:wght@500;700;800;900&family=Questrial&display=swap">
<style>
  :root {
    --navy: #141a63;
    --navy-light: #1f3a8f;
    --sky: #33a6d8;
    --red: #e3222b;
    --red-dark: #8e0a10;
    --red-band: #b51219;
    --mist: #f2f2f2;
    --mist-dark: #dcdcdc;
    --ink: #2b2b2b;
    --yellow: #fdd32e;
    --phone-yellow: #f9d423;
    --page: #e6e7e9;
    --white: #ffffff;
    --brand-blue: #2aa3d9;
  }
  * { box-sizing: border-box; margin: 0; padding: 0; }
  html, body {
    width: 1200px; height: 1200px; overflow: hidden;
    background: var(--page);
  }
  .postcard {
    position: absolute;
    left: 0; top: 138px;
    width: 1305px; height: 1004px;
    transform: scale(0.91954);
    transform-origin: 0 0;
    overflow: hidden;
    font-family: "Montserrat", sans-serif;
  }
  .postcard__art { position: absolute; inset: 0; }
  .text { position: absolute; white-space: nowrap; }

  .headline-lead {
    left: 48px; top: 96px;
    font-weight: 700; font-size: 34px; color: var(--white);
  }
  .headline-main {
    left: 46px; top: 132px;
    font-weight: 900; font-size: 70px; letter-spacing: -1px; line-height: 1;
  }
  .headline-main .free { color: var(--red); }
  .headline-main .roofs { color: #1fb4ee; }

  .facts {
    left: 0; width: 581px; text-align: center;
    font-family: "Questrial", sans-serif; font-size: 31px;
    color: var(--ink); line-height: 33px;
  }
  .facts strong { font-family: "Montserrat", sans-serif; font-weight: 700; }
  .facts .accent { color: #b3121a; }
  .facts--insurance { top: 318px; }
  .facts--claim { top: 439px; }

  .call-label {
    left: 50px; top: 591px;
    font-weight: 700; font-size: 38px; color: var(--white);
  }
  .call-phone {
    left: 48px; top: 628px;
    font-weight: 800; font-size: 70px; color: var(--phone-yellow);
    letter-spacing: -1px;
    text-shadow: 2px 3px 3px rgba(60, 0, 0, .55);
  }

  .license {
    left: 170px; top: 810px;
    font-family: "Questrial", sans-serif; font-size: 23px; color: var(--ink);
  }
  .brand {
    left: 56px; top: 846px;
    display: flex; align-items: center; gap: 18px;
  }
  .brand__mark { width: 34px; height: 34px; background: var(--red); flex: none; }
  .brand__name {
    font-weight: 700; font-size: 36px; line-height: 40px;
    color: var(--brand-blue); letter-spacing: -.3px;
  }

  .offer { left: 540px; width: 314px; text-align: center; }
  .offer__lead {
    top: 720px; font-family: "Questrial", sans-serif; font-size: 21px; color: #222;
  }
  .offer__price {
    top: 742px; font-weight: 900; font-size: 128px; line-height: 1;
    color: var(--red); letter-spacing: -4px;
    text-shadow: 3px 4px 3px rgba(90, 20, 0, .35);
  }
  .offer__price .currency {
    font-size: 46px; vertical-align: top; position: relative; top: 10px; margin-right: 2px;
  }
  .offer__title {
    top: 862px; font-weight: 700; font-size: 24px; color: #151515;
  }
  .offer__note {
    top: 888px; font-family: "Questrial", sans-serif; font-size: 19px; color: #151515;
  }
</style>
</head>
<body>
<main class="postcard">
  <svg class="postcard__art" viewBox="0 0 1305 1004" width="1305" height="1004">
    <defs>
      <linearGradient id="navyPanel" x1="0" y1="0" x2="1" y2="1">
        <stop offset="0" stop-color="#1f3a8f"/>
        <stop offset=".6" stop-color="#141a63"/>
      </linearGradient>
      <linearGradient id="mistPanel" x1="0" y1="0" x2="1" y2="0">
        <stop offset="0" stop-color="#dcdcdc"/>
        <stop offset=".45" stop-color="#f2f2f2"/>
        <stop offset="1" stop-color="#dcdcdc"/>
      </linearGradient>
      <linearGradient id="redBand" x1="0" y1="0" x2="0" y2="1">
        <stop offset="0" stop-color="#8e0a10"/>
        <stop offset=".5" stop-color="#b51219"/>
        <stop offset="1" stop-color="#8e0a10"/>
      </linearGradient>
      <linearGradient id="stormScene" x1="0" y1="0" x2="0" y2="1">
        <stop offset="0" stop-color="#25246e"/>
        <stop offset=".3" stop-color="#2d3f92"/>
        <stop offset=".5" stop-color="#2f4ea6"/>
        <stop offset=".66" stop-color="#26315c"/>
        <stop offset=".76" stop-color="#3f6a3a"/>
        <stop offset=".88" stop-color="#5a9a3c"/>
        <stop offset="1" stop-color="#6c9a58"/>
      </linearGradient>
      <radialGradient id="stormGlow" cx=".62" cy=".22" r=".45">
        <stop offset="0" stop-color="#9aa6e8" stop-opacity=".45"/>
        <stop offset="1" stop-color="#9aa6e8" stop-opacity="0"/>
      </radialGradient>
      <radialGradient id="badgeHalo" cx=".5" cy=".5" r=".5">
        <stop offset=".88" stop-color="#ffffff" stop-opacity=".95"/>
        <stop offset="1" stop-color="#dfeef6" stop-opacity=".7"/>
      </radialGradient>
    </defs>

    <rect x="0" y="0" width="900" height="282" fill="url(#navyPanel)"/>
    <rect x="0" y="282" width="581" height="258" fill="url(#mistPanel)"/>
    <rect x="0" y="540" width="581" height="5" fill="#c9c9c9"/>
    <rect x="0" y="545" width="581" height="211" fill="url(#redBand)"/>
    <rect x="0" y="756" width="581" height="248" fill="url(#mistPanel)"/>

    <polygon class="frame" fill="#33a6d8" points="581,163 782,0 1305,0 1305,1004 581,1004"/>

    <g class="storm-photo" role="img"
       aria-label="Photo of a blue two-storey house with a white-trimmed front porch, steps and green lawn under a dark stormy sky with rain and lightning">
      <polygon fill="url(#stormScene)" points="657,205 897,0 1305,0 1305,1004 1049,1004 1049,942 657,942"/>
      <polygon fill="url(#stormGlow)" points="657,205 897,0 1305,0 1305,1004 1049,1004 1049,942 657,942"/>
    </g>

    <line x1="300" y1="613" x2="532" y2="613" stroke="#ffffff" stroke-width="2"/>

    <circle cx="697" cy="810" r="166" fill="url(#badgeHalo)"/>
    <circle cx="697" cy="810" r="152" fill="#fdd32e"/>
    <circle cx="697" cy="810" r="143" fill="none" stroke="#c9a400" stroke-width="1.5" stroke-dasharray="5 4"/>
  </svg>

  <div class="text headline-lead">Local Residents are Getting</div>
  <div class="text headline-main"><span class="free">FREE</span> <span class="roofs">ROOFS!</span></div>

  <p class="text facts facts--insurance">Did You Know:<br>Storm Damage is Covered by<br>Your <strong class="accent">Homeowners Insurance</strong>?</p>
  <p class="text facts facts--claim">Do You Qualify for a <strong class="accent">FREE</strong> Roof?<br>Should You File a <strong>Claim</strong>?</p>

  <div class="text call-label">CALL TODAY</div>
  <div class="text call-phone">480-913-2748</div>

  <div class="text license">License number: ROC #284063</div>
  <div class="text brand">
    <span class="brand__mark"></span>
    <span class="brand__name">Tolvey Building<br>Partners</span>
  </div>

  <div class="text offer offer__lead">For a limited time...</div>
  <div class="text offer offer__price"><span class="currency">$</span>40</div>
  <div class="text offer offer__title">Storm damage</div>
  <div class="text offer offer__note">insurance inspection</div>
</main>
</body>
</html>
```